Business broker needs designs for business card, letterhead and email signature

I require the following items:
- business cards
- letterhead
- email signature

My company is a Business Broker company that specialises in business sales across various industries. The company has branches in four areas and each area has its own logo and website. Initially for the submission I am happy to inspect 1 design and 1 layout for quillharborgroup but the winner will need to complete a design for each area.

The four areas are:
1. quillharborgroup
2. tealridgefuelsales
3. orbvalechainsales
4. pondgrovegrocerdeals

I would like one design for each of the above items for each area. In each design, there should be one prominent logo and then the remaining three should also be included, for eg, the letterhead for the quillharborgrp area would have the quillharborgrp logo featuring prominently, somewhere at the top perhaps and the logos of the other three areas would be smaller and perhaps at the bottom, down the side, etc.

For the business cards, one prominent logo should feature on one side with the remaining three logos on the reverse.

The overall objective is for each item to look like it belongs to one family . I need all the source files as I may add new industries moving forward.

Target Market(s)

My company targets business minded people looking to increase wealth,. make an investment or migrate to Australia. People who busy and are looking for efficient and professional service in securing their next business venture.

Industry/Entity Type

Business

Font styles to use
Serif
Sans Serif

Requirements
Must have
• I want something professional and corporate looking, not something cartoony or playful. I am happy for you to be creative.

```html
<!DOCTYPE html>
<html lang="en">
<head>
<meta charset="utf-8">
<title>quillharborgroup stationery</title>
<link href="https://fonts.googleapis.com/css2?family=Arimo:wght@400;700&display=swap" rel="stylesheet">
<style>
  :root {
    --bg: #ececec;
    --paper: #ffffff;
    --ink: #2f3a45;
    --text: #333a40;
    --red: #c8102e;
    --pink: #e38a99;
    --yellow: #fad689;
    --teal: #9ee0d8;
    --green: #bcdf92;
    --orange: #f2a516;
    --tealdark: #2bb5ab;
    --greendark: #7cbf2a;
    --rule: #3a444d;
  }
  * { box-sizing: border-box; margin: 0; padding: 0; }
  html, body { width: 938px; height: 1200px; overflow: hidden; }
  body { background: var(--bg); font-family: "Arimo", Arial, sans-serif; color: var(--text); position: relative; }

  .letterhead { position: absolute; left: 40px; top: 24px; width: 858px; height: 1152px; background: var(--paper); }
  .colour-bar { display: flex; height: 19px; }
  .colour-bar span { flex: 1; }
  .c-pink { background: var(--pink); } .c-yellow { background: var(--yellow); }
  .c-teal { background: var(--teal); } .c-green { background: var(--green); }

  .brand { display: flex; align-items: center; gap: 12px; font-weight: 700; color: var(--ink); letter-spacing: -0.5px; }
  .brand-mark { flex: none; width: 14px; height: 14px; background: var(--red); }
  .brand-main { position: absolute; right: 28px; top: 62px; font-size: 38px; }
  .brand-main .brand-mark { width: 30px; height: 30px; }

  .footer { position: absolute; left: 0; right: 0; bottom: 0; height: 86px; border-top: 3px solid var(--rule); font-size: 13px; }
  .footer-row { position: absolute; right: 28px; display: flex; align-items: center; white-space: nowrap; }
  .row-1 { top: 16px; } .row-2 { top: 46px; }
  .item { display: flex; align-items: center; gap: 8px; }
  .sep { width: 1px; height: 16px; background: #888; margin: 0 34px; }
  .icon { width: 12px; height: 12px; fill: var(--red); flex: none; }

  .card { position: absolute; left: 18px; width: 344px; height: 200px; background: var(--paper); box-shadow: 0 0 0 1px #ddd; }
  .card-front { top: 390px; }
  .card-back { top: 630px; }
  .card .brand-card { position: absolute; right: 24px; top: 30px; font-size: 21px; gap: 8px; }
  .card .brand-card .brand-mark { width: 18px; height: 18px; }
  .card-name { position: absolute; left: 30px; top: 150px; font-size: 11.5px; color: var(--ink); }
  .card-name b { font-weight: 700; }
  .card-divider { position: absolute; left: 150px; top: 116px; width: 1px; height: 72px; background: #555; }
  .card-details { position: absolute; right: 22px; top: 80px; font-size: 9.5px; text-align: right; line-height: 1.3; }
  .card-details .item { justify-content: flex-end; margin-bottom: 6px; }
  .card-details .icon { width: 9px; height: 9px; }
  .card-details .acn { margin-bottom: 12px; }

  .area-list { position: absolute; left: 0; right: 0; top: 44px; display: flex; flex-direction: column; align-items: center; gap: 16px; }
  .area-list .brand { font-size: 18px; gap: 8px; }
  .area-list .brand-mark { width: 16px; height: 16px; }
  .area-orb .brand-mark { background: var(--orange); }
  .area-teal .brand-mark { background: var(--tealdark); }
  .area-pond .brand-mark { background: var(--greendark); }
  .card-back .colour-bar { position: absolute; left: 0; right: 0; bottom: 0; height: 7px; }
</style>
</head>
<body>
<svg width="0" height="0" style="position:absolute">
  <defs>
    <symbol id="i-mail" viewBox="0 0 12 12"><rect x="0" y="2" width="12" height="8" rx="1"/><path d="M0.5 2.5 6 7 11.5 2.5" fill="none" stroke="#fff" stroke-width="1.2"/></symbol>
    <symbol id="i-phone" viewBox="0 0 12 12"><path d="M3 0.5 5 3 3.8 4.6c.8 1.6 2 2.8 3.6 3.6L9 7l2.5 2-1.3 2.2C5.5 11 1 6.5.8 1.8Z"/></symbol>
    <symbol id="i-pin" viewBox="0 0 12 12"><path d="M6 0a4.3 4.3 0 0 0-4.3 4.3C1.7 7.5 6 12 6 12s4.3-4.5 4.3-7.7A4.3 4.3 0 0 0 6 0Zm0 6.2a1.9 1.9 0 1 1 0-3.8 1.9 1.9 0 0 1 0 3.8Z"/></symbol>
    <symbol id="i-web" viewBox="0 0 12 12"><circle cx="6" cy="6" r="5.2" fill="none" stroke="currentColor" stroke-width="1.4"/><path d="M0.8 6h10.4M6 0.8c-2.6 3-2.6 7.4 0 10.4M6 0.8c2.6 3 2.6 7.4 0 10.4" fill="none" stroke="currentColor" stroke-width="1.1"/></symbol>
  </defs>
</svg>

<main class="letterhead">
  <div class="colour-bar"><span class="c-pink"></span><span class="c-yellow"></span><span class="c-teal"></span><span class="c-green"></span></div>

  <div class="brand brand-main"><span class="brand-mark"></span>quillharborgroup</div>

  <footer class="footer">
    <div class="footer-row row-1">
      <span class="item">info@quillharborgroup.com.au <svg class="icon"><use href="#i-mail"/></svg></span>
      <span class="sep"></span>
      <span class="item">ACN:&nbsp; 284 519 307</span>
      <span class="sep"></span>
      <span class="item">1300 555 218 <svg class="icon"><use href="#i-phone"/></svg></span>
    </div>
    <div class="footer-row row-2">
      <span class="item">quillharborgroup.com.au <svg class="icon" style="color:var(--red)"><use href="#i-web"/></svg></span>
      <span class="item" style="margin-left:26px">Level 12, Harbour Tower, 88 Wharf Lane, Sydney NSW 2000 <svg class="icon"><use href="#i-pin"/></svg></span>
    </div>
  </footer>
</main>

<section class="card card-front">
  <div class="brand brand-card"><span class="brand-mark"></span>quillharborgroup</div>
  <p class="card-name"><b>Your Name,</b> Surname</p>
  <span class="card-divider"></span>
  <div class="card-details">
    <div class="item acn">ACN:&nbsp; 284 519 307</div>
    <div class="item">1300 555 218 <svg class="icon"><use href="#i-phone"/></svg></div>
    <div class="item">Level 12, Harbour Tower,<br>88 Wharf Lane, Sydney NSW 2000 <svg class="icon"><use href="#i-pin"/></svg></div>
    <div class="item">info@quillharborgroup.com.au <svg class="icon"><use href="#i-mail"/></svg></div>
    <div class="item">quillharborgroup.com.au <svg class="icon" style="color:var(--red)"><use href="#i-web"/></svg></div>
  </div>
</section>

<section class="card card-back">
  <div class="area-list">
    <div class="brand area-orb"><span class="brand-mark"></span>orbvalechainsales</div>
    <div class="brand area-teal"><span class="brand-mark"></span>tealridgefuelsales</div>
    <div class="brand area-pond"><span class="brand-mark"></span>pondgrovegrocerdeals</div>
  </div>
  <div class="colour-bar"><span class="c-pink"></span><span class="c-yellow"></span><span class="c-teal"></span><span class="c-green"></span></div>
</section>
</body>
</html>
```